Business Card Design Project

We need a Business Card for an Mechanical Engineering firm in Singapore. The design should be Modern & Technical looking, yet eye catching.

Our company deals in Cutting Tools & Machine Accessories for the Manufacturing Industries such as Oil & Gas, Aero Space, etc... For more information on our Company, you can either email me or view our website www.valtrion.com.sg.

We are trying to revamp our image to give our consumers a fresh new perspective to our company, so we welcome all ideas.

Industry/Entity Type

Business

Requirements
Must have
• Must incorporate New Company Logo into the card as shown in Uploaded file.

```html
<!DOCTYPE html>
<html lang="en">
<head>
<meta charset="utf-8">
<title>Valtrion Tools – Business Card</title>
<link rel="stylesheet" href="https://fonts.googleapis.com/css2?family=Signika:wght@300;400;600&display=swap">
<style>
  :root {
    --backdrop: #d9dadb;
    --card: #ffffff;
    --maroon: #951b34;
    --plum: #4b1529;
    --ink: #1a1a1a;
  }
  * { margin: 0; padding: 0; box-sizing: border-box; }
  html, body {
    width: 1200px; height: 900px; overflow: hidden;
    background: var(--backdrop);
    font-family: "Signika", "Helvetica Neue", Arial, sans-serif;
  }
  .card {
    position: absolute; left: 270px; width: 660px; height: 377px;
    background: var(--card);
  }
  .card--front { top: 45px; }
  .card--back { top: 478px; }

  .holder-name {
    position: absolute; left: 60px; top: 36px;
    font-size: 31px; font-weight: 300; color: var(--plum);
  }
  .name-rule {
    position: absolute; left: 0; top: 78px; width: 460px; height: 5px;
    background: var(--maroon);
  }
  .holder-title {
    position: absolute; left: 78px; top: 88px;
    font-size: 19px; font-weight: 300; color: var(--ink);
  }
  .contact {
    position: absolute; left: 78px; top: 151px;
    font-size: 17px; font-weight: 300; line-height: 22px;
    display: grid; grid-template-columns: 68px auto;
  }
  .contact dt { color: var(--ink); }
  .contact dd { color: var(--maroon); }

  .company {
    position: absolute; right: 420px; top: 264px; text-align: right;
  }
  .company-name {
    font-size: 21px; font-weight: 600; color: var(--plum); margin-bottom: 6px;
  }
  .company-address {
    font-style: normal; font-size: 17px; font-weight: 300;
    line-height: 21px; color: var(--maroon);
  }

  .brand {
    position: absolute; left: 266px; top: 140px; width: 380px; height: 220px;
  }
  .brand-dot {
    position: absolute; left: 150px; top: 20px; width: 90px; height: 90px;
    border-radius: 50%; background: var(--maroon);
  }
  .brand-name {
    position: absolute; left: 0; right: 0; top: 130px; text-align: center;
    font-size: 44px; font-weight: 400; color: var(--maroon); letter-spacing: 1px;
  }

  .back-rule {
    position: absolute; left: 0; top: 170px; width: 660px; height: 5px;
    background: var(--maroon);
  }
  .back-web {
    position: absolute; left: 330px; top: 180px; width: 330px; height: 58px;
    background: var(--maroon); color: #fff;
    font-size: 28px; font-weight: 300; letter-spacing: 1.5px;
    display: flex; align-items: center; justify-content: center;
  }
</style>
</head>
<body>
  <section class="card card--front">
    <h1 class="holder-name">Marcus Tan</h1>
    <div class="name-rule"></div>
    <p class="holder-title">President-CEO</p>
    <dl class="contact">
      <dt>mobile</dt><dd>65-63920418</dd>
      <dt>email</dt><dd>info@valtrion.com.sg</dd>
      <dt>web</dt><dd>www.valtrion.com.sg</dd>
    </dl>
    <div class="company">
      <p class="company-name">Valtrion Tools Pte Ltd</p>
      <address class="company-address">
        58 Kallang Way #03-12<br>
        Kallang Tech Centre<br>
        Singapore 349281
      </address>
    </div>
    <div class="brand">
      <span class="brand-dot"></span>
      <p class="brand-name">VALTRION TOOLS</p>
    </div>
  </section>

  <section class="card card--back">
    <div class="back-rule"></div>
    <p class="back-web">www.valtrion.com.sg</p>
  </section>
</body>
</html>
```